Flyer, poster, banner and social media titles designs for Community Renewal Guidlines

The Shared Guidelines for Community Renewal provide a nationally agreed framework to guide recovery policy and practice across Australia. The Principles support recovery practitioners, governments, non-government organisations and communities to deliver effective, community-centred recovery outcomes.
The Principles have recently been refreshed through extensive consultation and we require a contemporary visual identity and design suite that will increase awareness, engagement and practical application of the Principles.
The redesign will cover:
• A4 Brochure (primary publication)
• A3 Poster
• Pull up banner
• Social Media Tiles
The new design should:
• Create a recognisable brand for the Shared Guidelines.
• Appeal to both experienced and emerging recovery practitioners.
• Reflect contemporary Community Renewal practice.
• Feel people-focused rather than government-focused.
• Support future resources such as videos, implementation guides, presentations and workshop materials.
• Remain relevant for several years without requiring a major redesign.
Target Audience
• Community Renewal practitioners
• Government agencies
• Non-government organisations
• Community recovery workers
• Recovery managers and leaders
• Community stakeholders and volunteers
The visual identity should reflect the six Principles:
• Understanding Context
• Recognising Complexity
• Community-Centred Approaches
• Coordination
• Communication
• Capacity Building
The design should communicate:
• Recovery is centred on people and communities.
• Recovery is collaborative and involves many sectors.
• Recovery is adaptive, inclusive and evidence-informed.
• Recovery supports resilience and long-term wellbeing.
• The Principles provide practical guidance for recovery practice.
We are looking for:
• Modern and professional
• Warm and approachable
• Human-centred
• Inclusive and accessible
• Australian in context
• Visually engaging
• Suitable for print and digital use
We would like to avoid:
• Images of disaster destruction
• Emergency response imagery (fire trucks, flashing lights, etc.)
• Overly corporate or bureaucratic designs
• Designs that focus on deficits rather than recovery and growth
Consider themes such as:
• Connection and collaboration
• Communities and people
• Growth, recovery and renewal
Accessibility
Designs should:
• Meet accessibility best practice
• Use clear typography
• Achieve strong colour contrast
• Be suitable for both digital and print formats

Deliverables
1. Principles Brochure
• A4 trifold size x 2 (online and print friendly version)
• A side to include cover side, logos side and overview of principles.
• B side full details of the principles
• Graphic to highlight the 3 c’s concept (RECOVERY Context, complexity, community centred, coordinate, communicate and capacity). Currently 3 circles.
• Can be printed and distributed electronically
2. Poster
• A1 and A3 versions
• Suitable for office and workshop display
3. Pull-Up Banner - 850 mm (W) × 2000 mm (H)
• Conference and event use
• High visual impact
• Strong branding and concise messaging
4. Social Media Tiles x 3
Updates

We are providing an extension and increasing the budget following feedback from designers. We are wanting the resources to look and feel different from the existing designs, considering either a different colour palette in the designs or different motif with the leave design. Any nature based designs should consider the Australian fauna or flora. Also suggest avoiding images in the designs. The principles are not numbered or liner in the concept of how they function. Happy to answer any further questions and thank you for your suggested concepts.

Target Market(s)

Community Renewal practitioners, Government agencies , Non-government organisations, Community recovery workers and Community stakeholders and volunteers

Industry/Entity Type

Community Renewal

Colors

Designer to choose colors to be used in the design.

Requirements
Must have
• Modern, warm, visually engaging, human-centred, Australian in context and different to the current design.
Nice to have
• Symbols for each principles
Should not have
• Images of disaster destruction, Emergency response imagery, Overly corporate or bureaucratic designs, Designs that focus on deficits rather than recovery and growth, avoid too much black

```html
<!DOCTYPE html>
<html lang="en">
<head>
<meta charset="utf-8">
<title>Shared Guidelines for Community Renewal – Trifold Brochure</title>
<link href="https://fonts.googleapis.com/css2?family=Poppins:wght@300;400;500;600;700;800&family=Noto+Serif:wght@400&display=swap" rel="stylesheet">
<style>
  :root{
    --navy:#2b2565;
    --orange:#fba626;
    --tan:#c8935a;
    --white:#ffffff;
    --bg:#ededed;
    --ink:#2b2565;
    --faint-navy:rgba(43,37,101,.07);
    --faint-white:rgba(255,255,255,.10);
  }
  *{box-sizing:border-box;margin:0;padding:0}
  html,body{width:1200px;height:1200px;overflow:hidden;background:var(--bg)}
  body{position:relative;font-family:'Poppins',sans-serif;color:var(--ink)}
  .sheet{position:absolute;width:704px;height:497px;overflow:hidden;background:var(--white)}
  .sheet-front{left:131px;top:86px}
  .sheet-back{left:365px;top:618px}
  .abs{position:absolute}
  .panel{position:absolute;top:0;height:100%;width:235px;overflow:hidden}
  .wordmark{font-family:'Noto Serif',serif;line-height:.95;color:var(--white)}

  /* ---------- front: intro panel ---------- */
  .panel-intro{left:0;background:var(--orange)}
  .panel-intro .wordmark{right:15px;top:42px;font-size:15px;text-align:right}
  .tag{background:var(--navy);color:var(--orange);font-weight:500;letter-spacing:.3px;white-space:nowrap}
  .panel-intro .tag{right:15px;top:95px;font-size:9.5px;padding:1px 8px}
  .word{font-weight:700;line-height:1;white-space:nowrap}
  .vert{writing-mode:vertical-rl;transform:rotate(180deg);font-weight:700;white-space:nowrap}
  .intro-text{left:24px;top:229px;width:186px;color:var(--white);font-size:5.2px;font-weight:300;line-height:1.45}
  .intro-text p{margin-bottom:3px}
  .relation-box{left:0;top:356px;width:265px;height:111px;background:var(--navy);border-radius:0 10px 10px 0;z-index:3}
  .relation-box .dots{left:20px;top:11px;width:6px}
  .relation-box .dots span{display:block;width:4px;height:4px;border-radius:50%;background:var(--orange);margin-bottom:4.5px}
  .relation-box .line{left:22px;top:48px;width:1px;height:50px;background:var(--orange)}
  .relation-box h3{left:35px;top:11px;color:var(--white);font-size:8px;font-weight:600;line-height:1.25}
  .relation-box .body{left:35px;top:36px;width:180px;color:var(--white);font-size:6.2px;font-weight:300;line-height:1.35}
  .relation-box .body p{margin-bottom:4px}
  .relation-box .vert{left:247px;top:10px;height:92px;color:var(--orange);font-size:5.6px;line-height:1.2;font-weight:600}

  /* ---------- front: partners panel ---------- */
  .panel-partners{left:235px;background:var(--white)}
  .partner-grid{left:22px;top:78px;width:200px;display:grid;grid-template-columns:repeat(3,1fr);row-gap:20px;column-gap:6px}
  .partner{display:flex;flex-direction:column;align-items:center;gap:3px;text-align:center;font-size:5.2px;font-weight:600;color:var(--navy);line-height:1.2}
  .partner i{display:block;width:20px;height:20px;border-radius:50%;background:var(--navy)}
  .partner-wide{left:28px;top:282px;display:flex;align-items:center;gap:6px;font-size:7px;font-weight:600;color:var(--navy)}
  .partner-wide i{width:16px;height:16px;background:var(--navy);display:block}
  .partner-feature{left:42px;top:420px;display:flex;align-items:center;gap:8px;font-size:7.5px;color:var(--navy);line-height:1.3}
  .partner-feature i{width:36px;height:36px;border-radius:50%;border:0;background:#5fb3d6;display:block}
  .partner-feature small{font-size:5px;letter-spacing:1px}
  .ghost{color:var(--faint-navy);font-weight:700;line-height:1;white-space:nowrap}
  .foliage-b{left:145px;top:0;width:90px;height:75px;background:linear-gradient(200deg,#6fbf4a 0%,rgba(111,191,74,.35) 55%,rgba(255,255,255,0) 100%)}

  /* ---------- front: cover panel ---------- */
  .panel-cover{left:469px;background:var(--navy)}
  .foliage-c{left:0;top:0;width:235px;height:143px;background:linear-gradient(160deg,#3a8a3a 0%,#f5a623 45%,rgba(43,37,101,0) 90%)}
  .cover-eyebrow{left:40px;top:159px;color:var(--orange);font-size:10.5px;font-weight:400;letter-spacing:.2px}
  .panel-cover .wordmark{left:38px;top:178px;font-size:33px}
  .panel-cover .tag{left:0;top:266px;width:212px;height:26px;background:var(--orange);color:var(--navy);font-size:16px;font-weight:600;display:flex;align-items:center;justify-content:center}

  /* ---------- back ---------- */
  .col-navy{left:0;top:0;width:235px;height:497px;background:var(--navy)}
  .rule{height:1.5px;background:var(--orange)}
  .sec-kicker{font-size:8.5px;font-weight:400;color:var(--orange)}
  .sec-title{font-size:13.5px;font-weight:700;line-height:1}
  .sec-sub{font-size:8.5px;font-weight:400}
  .lead{font-size:5.2px;line-height:1.3;color:var(--orange);width:46px}
  .lead b{font-weight:700}
  .bullets{list-style:none;font-size:5px;line-height:1.25;font-weight:400}
  .bullets li{position:relative;padding-left:7px;margin-bottom:3.5px}
  .bullets li::before{content:"•";position:absolute;left:0}
  .on-navy{color:var(--white)}
  .on-white{color:#333}
  .icon{width:36px;height:36px;border-radius:50%;background:var(--orange)}
  .icon svg{width:36px;height:36px;display:block}
  .back-mark{left:24px;top:455px;font-size:14px}
</style>
</head>
<body>

<!-- ================= FRONT SIDE ================= -->
<section class="sheet sheet-front" aria-label="Brochure side A">

  <div class="panel panel-intro">
    <div class="abs wordmark">Community<br>Renewal</div>
    <div class="abs vert" style="left:70px;top:88px;font-size:20px;color:var(--navy)">NTEXT</div>
    <div class="abs tag">Successful Recovery</div>
    <div class="abs word" style="right:15px;top:113px;font-size:21px;color:var(--white)">COMPLECITY</div>
    <div class="abs word" style="right:15px;top:138px;font-size:15px;color:var(--navy)">COMMUNITY</div>
    <div class="abs word" style="right:15px;top:152px;font-size:15px;color:var(--navy)">-LED</div>
    <div class="abs word" style="left:14px;top:130px;font-size:78px;color:var(--white);font-weight:600">C</div>
    <div class="abs word" style="left:54px;top:154px;font-size:19px;color:var(--white)">OORDINATE</div>
    <div class="abs word" style="left:74px;top:170px;font-size:20px;color:var(--navy)">OMMUNICATE</div>
    <div class="abs word" style="left:44px;top:184px;font-size:36px;color:var(--white);font-weight:600">A</div>
    <div class="abs word" style="left:74px;top:190px;font-size:26px;color:var(--white)">PACITY</div>

    <div class="abs intro-text">
      <p>Disasters can deeply impact lives and livelihoods. Working with communities recovering from disasters is complex and challenging. These principles are a way to guide our efforts, our approach, our planning and our decision-making.</p>
      <p>Disaster recovery is part of emergency management, which includes the broader components of prevention, preparedness and response. Planning for recovery is integral to emergency preparation and mitigation actions may often be initiated as part of recovery.</p>
      <p>Disaster recovery includes built, environmental and economic elements, all contributing to individual and social wellbeing.</p>
      <p>Recovery can provide an opportunity to improve these aspects beyond previous conditions, contributing to a more resilient community.</p>
    </div>
  </div>

  <div class="panel panel-partners">
    <div class="abs foliage-b" role="img" aria-label="Wattle and gum leaf illustration"></div>
    <div class="abs partner-grid">
      <div class="partner"><i></i>Federal Care<br>Office</div>
      <div class="partner"><i></i>Harbour Aid</div>
      <div class="partner"><i></i>Southland<br>Council</div>
      <div class="partner"><i></i>Federal Safety<br>Office</div>
      <div class="partner"><i></i>Westland<br>Council</div>
      <div class="partner"><i></i>Island State<br>Office</div>
      <div class="partner"><i></i>Top End<br>Office</div>
      <div class="partner"><i></i>Sunbelt State<br>Office</div>
      <div class="partner"><i></i>Capital Region<br>Office</div>
      <div class="partner"><i></i>Coastal State<br>Office</div>
    </div>
    <div class="abs partner-wide"><i></i>Eastern Resilience Office</div>
    <div class="abs vert" style="left:224px;top:300px;font-size:34px;color:rgba(251,166,38,.15)">NTEXT</div>
    <div class="abs ghost" style="left:-8px;top:330px;font-size:150px">C</div>
    <div class="abs ghost" style="left:32px;top:370px;font-size:28px;color:rgba(251,166,38,.18)">OOR</div>
    <div class="abs ghost" style="left:32px;top:395px;font-size:28px;color:rgba(251,166,38,.14)">CO</div>
    <div class="abs ghost" style="left:45px;top:405px;font-size:60px">A</div>
    <div class="abs partner-feature"><i></i><span>Renewal Practice<br>Network<br><small>AUSTRALIA</small></span></div>
  </div>

  <div class="panel panel-cover">
    <div class="abs foliage-c" role="img" aria-label="Wattle blossom and gum leaf illustration"></div>
    <div class="abs cover-eyebrow">SHARED GUIDELINES FOR</div>
    <div class="abs wordmark">Community<br>Renewal</div>
    <div class="abs tag">Successful Recovery</div>
    <div class="abs word" style="left:0;top:299px;font-size:30px;color:var(--white)">COMPLECITY</div>
    <div class="abs word" style="right:23px;top:336px;font-size:22px;color:var(--tan)">COMMUNITY</div>
    <div class="abs word" style="right:23px;top:358px;font-size:22px;color:var(--tan)">-LED</div>
    <div class="abs word" style="left:0;top:360px;font-size:29px;color:var(--faint-white)">DINATE</div>
    <div class="abs word" style="left:4px;top:393px;font-size:32px;color:var(--orange)">MMUNICATE</div>
    <div class="abs word" style="left:-6px;top:428px;font-size:44px;color:rgba(255,255,255,.3)">PACITY</div>
  </div>

  <div class="abs relation-box">
    <div class="abs dots"><span></span><span></span><span></span><span></span></div>
    <div class="abs line"></div>
    <h3 class="abs">THE RELATIONSHIP BETWEEN<br>THE PRINCIPLES</h3>
    <div class="abs body">
      <p>While all the principles are equally critical to ensure effective recovery, understanding the local and broader <b>context</b> and recognising <b>complexity</b> are foundational.</p>
      <p>The descriptions beneath each principle overleaf provide further guidance for working with communities in disaster recovery.</p>
    </div>
    <div class="abs vert">PARTNERS IN<br>DEVELOPMENT FROM THE</div>
  </div>
</section>

<!-- ================= BACK SIDE ================= -->
<section class="sheet sheet-back" aria-label="Brochure side B">
  <div class="abs col-navy"></div>
  <div class="abs ghost" style="left:30px;top:300px;font-size:190px;color:rgba(255,255,255,.05)">C</div>
  <div class="abs ghost" style="left:150px;top:380px;font-size:140px;color:rgba(43,37,101,.08)">APACITY</div>
  <div class="abs ghost" style="left:270px;top:180px;font-size:56px;color:rgba(43,37,101,.05)">COMPLECITY</div>
  <div class="abs ghost" style="left:180px;top:290px;font-size:50px;color:rgba(251,166,38,.06)">ORDINATE</div>

  <!-- context -->
  <div class="abs sec-kicker" style="left:24px;top:27px">Understand the</div>
  <div class="abs sec-title" style="left:76px;top:38px;color:var(--orange)">CONTEXT</div>
  <div class="abs rule" style="left:76px;top:57px;width:159px"></div>
  <div class="abs lead" style="left:24px;top:69px"><b>Successful recovery</b> is based on an understanding of the community context, with each community having its own history, values and dynamics</div>
  <ul class="abs bullets on-navy" style="left:76px;top:68px;width:145px">
    <li>Acknowledge existing strengths and capacity, including past experiences;</li>
    <li>Appreciate the risks and stressors faced by the community;</li>
    <li>Be respectful of and sensitive to the culture and diversity of the community;</li>
    <li>Support those who may be facing vulnerability;</li>
    <li>Recognise the importance of the environment to people and to their recovery;</li>
    <li>Be acknowledged as requiring a long term sustained effort as needed by the community; and</li>
    <li>Acknowledge that the impact upon the community may extend beyond the geographical boundaries where the disaster occurred.</li>
  </ul>
  <div class="abs icon" style="left:23px;top:162px"><svg viewBox="0 0 36 36"><g fill="none" stroke="#fff" stroke-width="1.3"><rect x="10" y="10" width="6" height="6"/><rect x="20" y="20" width="6" height="6"/><path d="M16 13h7v7M13 16v7h7"/></g></svg></div>

  <!-- complexity -->
  <div class="abs sec-kicker" style="left:24px;top:229px">RECOGNISE</div>
  <div class="abs sec-title" style="left:76px;top:240px;color:var(--orange)">COMPLEXITY</div>
  <div class="abs rule" style="left:76px;top:260px;width:159px"></div>
  <div class="abs lead" style="left:24px;top:271px"><b>Successful recovery</b> is responsive to the complex and dynamic nature of both emergencies and the community.</div>
  <ul class="abs bullets on-navy" style="left:76px;top:270px;width:145px">
    <li>Disasters lead to a range of effects and impacts that require a variety of approaches; they can also leave long-term legacies;</li>
    <li>Information on impacts is limited at first and changes over time;</li>
    <li>Affected individuals and the community have diverse needs, wants and expectations, which can evolve rapidly;</li>
    <li>Responsive and flexible action is crucial to address immediate needs;</li>
    <li>Existing community knowledge and values may challenge the assumptions of those outside of the community;</li>
    <li>Conflicting knowledge, values and priorities among individuals, the community and organisations may create tensions;</li>
    <li>Emergencies create stressful environments where grief or blame may also affect those involved; and</li>
    <li>Over time, appropriate support for individuals and communities, from within and outside, can cultivate hope and individual and collective growth.</li>
  </ul>
  <div class="abs icon" style="left:23px;top:392px"><svg viewBox="0 0 36 36"><g fill="none" stroke="#fff" stroke-width="1.3"><rect x="10" y="10" width="7" height="7"/><rect x="19" y="10" width="7" height="7"/><rect x="10" y="19" width="7" height="7"/><rect x="19" y="19" width="7" height="7"/></g></svg></div>
  <div class="abs wordmark back-mark">Community<br>Renewal</div>

  <!-- community-led -->
  <div class="abs" style="left:249px;top:28px;font-size:8px;color:var(--navy)">use <span class="sec-title">COMMUNITY-LED</span></div>
  <div class="abs sec-sub" style="left:302px;top:42px;color:var(--navy)">approaches</div>
  <div class="abs lead" style="left:249px;top:69px"><b>Successful recovery</b> is community-centred, responsive and flexible, engaging with community and supporting them to move forward.</div>
  <ul class="abs bullets on-white" style="left:302px;top:68px;width:150px">
    <li>Assist and enable individuals, families and the community to actively participate in their own recovery;</li>
    <li>Recognise that individuals and the community may need different levels of support at various times;</li>
    <li>Be guided by the community's priorities;</li>
    <li>Channel effort through pre-identified and existing community assets, including local knowledge, existing community strengths and resilience;</li>
    <li>Build collaborative partnerships between the community and those involved in the recovery process;</li>
    <li>Recognise that new community leaders often emerge during and after a disaster, who may not hold formal positions of authority; and</li>
    <li>Recognise that different communities may choose different paths to recovery.</li>
  </ul>
  <div class="abs icon" style="left:249px;top:162px"><svg viewBox="0 0 36 36"><g fill="none" stroke="#fff" stroke-width="1.3"><circle cx="18" cy="14" r="4"/><path d="M11 26c0-4 3-6 7-6s7 2 7 6"/></g></svg></div>

  <!-- communicate -->
  <div class="abs sec-title" style="left:484px;top:28px;color:var(--navy)">COMMUNICATE</div>
  <div class="abs sec-sub" style="left:538px;top:42px;color:var(--navy)">effectively</div>
  <div class="abs lead" style="left:484px;top:69px"><b>Successful recovery</b> is built on effective communication between the affected community and other partners.</div>
  <ul class="abs bullets on-white" style="left:538px;top:68px;width:150px">
    <li>Recognise that communication should be two-way, and that input and feedback should be encouraged;</li>
    <li>Ensure that information is accessible to audiences in diverse situations, addresses a variety of communication needs, and is provided through a range of media and networks;</li>
    <li>Establish mechanisms for coordinated and consistent communications between all service providers, organisations and individuals and the community;</li>
    <li>Ensure that all communication is relevant, timely, clear, accurate, targeted, credible and consistent; and</li>
    <li>Identify trusted sources of information and repeat key recovery messages to enable greater community confidence and receptivity.</li>
  </ul>
  <div class="abs icon" style="left:484px;top:162px"><svg viewBox="0 0 36 36"><g fill="none" stroke="#fff" stroke-width="1.3"><path d="M10 12h14v9h-8l-4 4v-4h-2z"/><path d="M26 16h2v9h-2v3l-3-3"/></g></svg></div>

  <div class="abs rule" style="left:235px;top:57px;width:469px"></div>

  <!-- coordinate -->
  <div class="abs sec-title" style="left:249px;top:230px;color:var(--navy)">COORDINATE</div>
  <div class="abs sec-sub" style="left:302px;top:244px;color:var(--navy)">all activities</div>
  <div class="abs lead" style="left:249px;top:271px"><b>Successful recovery</b> requires a planned, coordinated and adaptive approach, between community and partner agencies, based on continuing assessment of impacts and need</div>
  <ul class="abs bullets on-white" style="left:302px;top:270px;width:150px">
    <li>Have clearly articulated and shared goals based on desired outcomes;</li>
    <li>Be flexible, taking into account changes in community needs or stakeholder expectations; be guided by those with experience and expertise, using skilled, authentic and capable community leadership;</li>
    <li>Be at the pace desired by the community, and seek to collaborate and reconcile different interests and time frames;</li>
    <li>Reflect well-developed community planning and information gathering before, during and after a disaster;</li>
    <li>Have clear decision-making and reporting structures and sound governance, which are transparent and accessible to the community;</li>
    <li>Demonstrate an understanding of the roles, responsibilities and authority of organisations involved and coordinate across agencies to ensure minimal service provision disruption;</li>
    <li>Be part of an emergency management approach that integrates with response operations and contributes to future prevention and preparedness; and</li>
    <li>Be inclusive, availing of and building upon relationships created before, during and after the emergency.</li>
  </ul>
  <div class="abs icon" style="left:249px;top:392px"><svg viewBox="0 0 36 36"><g fill="none" stroke="#fff" stroke-width="1.3"><circle cx="18" cy="18" r="4"/><circle cx="18" cy="18" r="8" stroke-dasharray="3 2"/></g></svg></div>

  <!-- capacity -->
  <div class="abs sec-kicker" style="left:484px;top:229px;color:var(--navy)">Recognise and build</div>
  <div class="abs sec-title" style="left:538px;top:240px;color:var(--navy)">CAPACITY</div>
  <div class="abs lead" style="left:484px;top:271px"><b>Successful recovery</b> recognises, supports and builds on individual, community and organisational capacity and resilience.</div>
  <ul class="abs bullets on-white" style="left:538px;top:270px;width:150px">
    <li>Assess capability and capacity requirements before, during and after a disaster;</li>
    <li>Support the development of self-reliance, preparation and disaster mitigation; quickly identify and mobilise community skills, strengths and resources;</li>
    <li>Develop networks and partnerships to strengthen capacity, capability and resilience;</li>
    <li>Provide opportunities to share, transfer and develop knowledge, skills and training;</li>
    <li>Recognise that resources can be provided by a range of partners and from community networks;</li>
    <li>Acknowledge that existing resources may be stretched, and that additional resources may be sought;</li>
    <li>Understand that additional resources may only be available for a limited period, and that sustainability may need to be addressed;</li>
    <li>Understand when and how to step back, while continuing to support individuals and the community as a whole to be more self-sufficient when they are ready; and</li>
    <li>Be evaluated to provide learning for future and improved resilience.</li>
  </ul>
  <div class="abs icon" style="left:484px;top:392px"><svg viewBox="0 0 36 36"><g fill="none" stroke="#fff" stroke-width="1.3"><path d="M13 11v14M18 11v14M23 11v14"/><path d="M11 15h4M16 21h4M21 17h4"/></g></svg></div>

  <div class="abs rule" style="left:235px;top:260px;width:469px"></div>
</section>

</body>
</html>
```